Letterhead and Corporate Stationary Design Project

I would like the following designed:
1. Corporate Letterhead
2. Compliment Slips
3. Business Cards(2)

I have attached word document that outlines the text to be contained for all 3. The logo is fine as is and can be used in the design.
I only need letterhead to be designed for contest, the successful applicant can desisgn other 2 items after being awarded the job

Target Market(s)

Information Technology

Industry/Entity Type

Business

Requirements
Must have
• Border around entire letter that matches colours in logo
Clearly identifiable letterhead and footer
Nice to have
• Watermark

```html
<!DOCTYPE html>
<html lang="en">
<head>
<meta charset="utf-8">
<title>Corvane Business Solutions – Letterhead</title>
<link href="https://fonts.googleapis.com/css2?family=Arimo:wght@400;700&family=Nothing+You+Could+Do&display=swap" rel="stylesheet">
<style>
  :root {
    --backdrop: #a4ac93;
    --paper: #ffffff;
    --ink: #1a1a1a;
    --brand-blue: #0a3be8;
    --brand-sky: #35a9f0;
    --rule-navy: #1c2a8c;
    --footer-text: #dfe6ff;
  }
  * { margin: 0; padding: 0; box-sizing: border-box; }
  html, body { width: 1200px; height: 900px; overflow: hidden; }
  body {
    background: var(--backdrop);
    font-family: "Arimo", Arial, sans-serif;
    color: var(--ink);
    position: relative;
  }
  .letterhead {
    position: absolute;
    left: 333px; top: 52px;
    width: 544px; height: 772px;
    background: var(--paper);
  }
  .brand {
    position: absolute;
    left: 25px; top: 42px;
    display: flex; align-items: center; gap: 8px;
  }
  .brand-dot {
    width: 26px; height: 26px; border-radius: 50%;
    background: var(--brand-sky);
  }
  .brand-name {
    font-size: 19px; font-weight: 700; color: var(--brand-blue);
    letter-spacing: 0.2px;
  }
  .sender {
    position: absolute;
    right: 26px; top: 34px;
    text-align: right;
    font-size: 8px; line-height: 10px;
  }
  .header-rule {
    position: absolute;
    left: 25px; right: 26px; top: 91px;
    height: 1px; background: var(--rule-navy);
  }
  .letter {
    position: absolute;
    left: 25px; right: 26px; top: 123px;
    font-size: 8px; line-height: 9.7px;
  }
  .salutation { font-weight: 700; font-size: 8.5px; margin-bottom: 11px; }
  .letter p { text-align: justify; margin-bottom: 9.7px; }
  .signature {
    font-family: "Nothing You Could Do", cursive;
    font-size: 17px; line-height: 18px; margin-top: 12px;
  }
  .role { font-weight: 700; font-size: 8px; }
  .footer-band {
    position: absolute;
    left: 0; right: 0; bottom: 0; height: 56px;
    background: var(--brand-blue);
    display: flex; align-items: center; justify-content: center;
    color: var(--footer-text); font-size: 7.5px;
  }
</style>
</head>
<body>
  <main class="letterhead">
    <div class="brand">
      <span class="brand-dot"></span>
      <span class="brand-name">Corvane Business Solutions</span>
    </div>
    <address class="sender" style="font-style:normal">
      Corvane Business Solutions<br>
      Harbour House, 8 Quay Street, Kilmore<br>
      Co. Wexford, Ireland<br>
      tel:&nbsp; + 353 41 555 0183<br>
      www.corvane.ie
    </address>
    <div class="header-rule"></div>

    <article class="letter">
      <p class="salutation">Lorem ipsum,</p>
      <p>Lorem ipsum dolor sit amet, consectetur adipiscing elit. In sit amet ipsum purus. Sed imperdiet vulputate nisi, in aliquam mauris varius et. Morbi a nisi ac ligula gravida auctor sed sed elit. Nam ac nunc sit amet neque scelerisque tristique vel ut ligula. Mauris nec ipsum sapien, vel tincidunt sapien. Pellentesque sit amet lorem eros, rutrum sagittis ligula. Phasellus at neque id felis adipiscing pulvinar nec id mauris. In hac habitasse platea dictumst. Nam fermentum iaculis malesuada. Mauris vitae odio at sem ornare tempor in vel odio. Ut venenatis pellentesque. Sed tincidunt leo id elit scelerisque vestibulum.</p>
      <p>Vestibulum ultrices nunc sed urna tincidunt ut faucibus elit molestie. Integer ultrices mauris at lacus ultrices egestas. Phasellus in dui nulla. Cras justo est, volutpat in semper sit amet, viverra vel purus. Vestibulum eget odio odio. Pellentesque gravida arcu eu lectus accumsan et lobortis tortor fringilla. Curabitur ultricies tempus elit, ut congue diam porta sed. Quisque nec felis quam, at mollis nisl. Curabitur rutrum libero eu justo congue pulvinar nec eu magna. Nunc vel augue in nunc lacinia tincidunt nec sit amet ligula. Vivamus consequat sollicitudin semper.</p>
      <p>Vivamus lobortis tincidunt tellus quis sodales. Nullam sodales lacinia libero. Vivamus rhoncus quam a urna porta tempus. Proin arcu metus, cursus vel ornare eu, posuere id augue. Suspendisse auctor posuere mauris, rutrum luctus augue vehicula a. Maecenas id tristique est. Sed a felis dolor, et placerat lacus. Cras commodo nunc eu velit iaculis ut porta tortor laoreet. Integer bibendum nunc at sapien consectetur vel scelerisque dolor suscipit. Nam sagittis risus id ante auctor ut fermentum sapien lacinia.</p>
      <p>Sed viverra condimentum dolor, et condimentum justo accumsan in. Aliquam erat volutpat. Nullam quis justo elit. Nullam nec turpis augue, in ultrices purus. Suspendisse nulla dolor, mollis commodo faucibus at, malesuada in arcu. Nam quis vehicula justo. Donec pretium egestas justo a dictum. Nam sit amet euismod elit. Curabitur a mi id ipsum vehicula pharetra at quis urna. Etiam suscipit, quam ut rutrum lacinia, dui tellus luctus enim, vel consequat magna mi rutrum sapien. Ut urna velit, accumsan sed consequat eget, malesuada non odio.</p>
      <p>Suspendisse vitae viverra risus. Integer ultricies tristique risus id dapibus. Donec non dolor lacus, eget cursus quam. Sed pharetra posuere consectetur. Proin sit amet diam nisl, eu sodales leo. Ut est mauris, aliquam id gravida at, sagittis at tortor. Quisque commodo euismod nisl id convallis. Aenean sed felis nec ligula elementum pellentesque sed in enim. Integer ac rhoncus velit.</p>
      <div class="signature">Your name</div>
      <div class="role">Manager</div>
    </article>

    <footer class="footer-band">
      Corvane Business Solutions Limited • Company Registration 512904 • VAT No IE5129041K
    </footer>
  </main>
</body>
</html>
```